Newsletter Ad

I am looking for someone to design an advertisement for a mother's club newsletter. 4" wide X by 5" tall (and 2.5" wide X 5" tall if possible).

I'm a psychotherapist, so want the ad to look professional, but modern. I have a logo with my photo attached that can be incorporated into the design. The colors of my website are turquoise and white. I'd like to keep with that theme...so maybe some turquoise blocking to match the logo font color.

I'm uploading a logo as well as an ad draft with the content I'd like listed in the ad.

```html
<!DOCTYPE html>
<html lang="en">
<head>
<meta charset="utf-8">
<title>Psychotherapy Newsletter Ad</title>
<link rel="stylesheet" href="https://fonts.googleapis.com/css2?family=Open+Sans:ital,wght@0,400;0,600;0,700;1,400&family=Quicksand:wght@400&display=swap">
<style>
  :root {
    --backdrop: #5a5b5d;
    --teal: #2e9896;
    --teal-text: #2f9a98;
    --mist: #d6e3e4;
    --paper: #ffffff;
    --ink: #111111;
    --photo-dark: #2b2420;
    --photo-light: #a88868;
  }
  * { margin: 0; padding: 0; box-sizing: border-box; }
  html, body { width: 1200px; height: 906px; overflow: hidden; background: var(--backdrop); }
  body { position: relative; font-family: "Open Sans", Arial, sans-serif; }

  .ad { position: absolute; top: 56px; height: 801px; background: var(--paper); overflow: hidden; }
  .ad--tall { left: 64px; width: 641px; }
  .ad--narrow { left: 742px; width: 400px; }

  .ad__shapes { position: absolute; inset: 0; width: 100%; height: 100%; }

  .headline { position: absolute; left: 0; right: 0; text-align: center; color: var(--paper); font-weight: 700; line-height: 1; }
  .headline__main { display: block; }
  .headline__sub { display: block; }

  .portrait { position: absolute; background: linear-gradient(135deg, var(--photo-dark) 0%, var(--photo-light) 55%, var(--photo-dark) 100%); }

  .therapist-name { position: absolute; font-family: "Quicksand", "Century Gothic", sans-serif; font-weight: 400; color: var(--teal-text); white-space: nowrap; line-height: 1; letter-spacing: 0.5px; }

  .contact { position: absolute; color: var(--ink); line-height: 1; }
  .contact__line { position: absolute; left: 0; white-space: nowrap; }
  .contact__web { color: var(--teal-text); font-weight: 700; letter-spacing: 0.6px; }
  .contact__phone { font-weight: 700; letter-spacing: 1.4px; }

  .services { position: absolute; list-style: none; color: var(--teal-text); font-weight: 700; line-height: 1; }
  .services li { position: absolute; white-space: nowrap; }

  .ad--tall .services li { left: 0; }
  .ad--tall .services li::before { content: "•"; position: absolute; left: -18px; }
  .ad--tall .services li.services__cont::before { content: none; }
  .ad--narrow .services { left: 0; right: 0; }
  .ad--narrow .services li { left: 0; right: 0; text-align: center; }

  .license { position: absolute; font-style: italic; font-size: 14px; color: var(--ink); white-space: nowrap; line-height: 1; }
</style>
</head>
<body>

<section class="ad ad--tall">
  <svg class="ad__shapes" viewBox="0 0 641 801" aria-hidden="true">
    <polygon points="0,0 641,0 641,163 454,163 0,270" fill="var(--teal)"/>
    <path d="M0,553 C40,540 90,560 130,590 C175,625 210,640 270,640 C340,640 380,660 420,710 C445,742 460,765 470,776 L0,776 Z" fill="var(--mist)"/>
    <rect x="0" y="776" width="641" height="25" fill="var(--teal)"/>
    <g fill="none" stroke="var(--mist)" stroke-width="10">
      <circle cx="538" cy="405" r="28"/>
      <circle cx="565" cy="422" r="28"/>
    </g>
    <g fill="none" stroke="var(--paper)" stroke-width="10" opacity="0.85" transform="rotate(-35 72 650)">
      <circle cx="72" cy="650" r="31"/>
      <line x1="72" y1="681" x2="72" y2="745"/>
      <line x1="50" y1="716" x2="94" y2="716"/>
    </g>
  </svg>

  <h1 class="headline" style="top:62px;">
    <span class="headline__main" style="font-size:42px;">Psychotherapy <span style="font-size:26px;">for</span></span>
    <span class="headline__sub" style="font-size:26px; margin-top:10px;">Individuals, Couples and Families</span>
  </h1>

  <div class="portrait" style="left:65px; top:212px; width:156px; height:156px;" role="img" aria-label="Portrait photo of the therapist"></div>

  <div class="therapist-name" style="left:243px; top:262px; font-size:34px;">DANA REED, MA, MFT</div>

  <div class="contact" style="left:57px; top:0;">
    <span class="contact__line" style="top:395px; font-size:15.5px;">418 Harbor Lane,</span>
    <span class="contact__line" style="top:418px; font-size:15.5px;">Cedar Grove, CA 94000</span>
    <span class="contact__line contact__web" style="top:451px; font-size:15.5px;">www.danareed.com</span>
    <span class="contact__line" style="top:489px; font-size:15.5px;">dana@danareed.com</span>
    <span class="contact__line contact__phone" style="top:512px; font-size:18px;">415.555.0182</span>
  </div>

  <ul class="services" style="left:281px; top:0; font-size:24px;">
    <li style="top:365px;">Parenting</li>
    <li style="top:401px;">Depression</li>
    <li style="top:436px;">Anxiety</li>
    <li style="top:472px;">Life Transitions</li>
    <li style="top:508px;">Divorce</li>
    <li style="top:544px;">Couples Issues</li>
    <li style="top:580px;">Women’s Issues</li>
    <li style="top:615px;">Attachment</li>
    <li class="services__cont" style="top:651px;">and Neuroscience</li>
  </ul>

  <div class="license" style="right:35px; top:734px;">License# MFC48210</div>
</section>

<section class="ad ad--narrow">
  <svg class="ad__shapes" viewBox="0 0 400 801" aria-hidden="true">
    <polygon points="0,0 400,0 400,163 0,203" fill="var(--teal)"/>
    <rect x="0" y="776" width="400" height="25" fill="var(--teal)"/>
    <g fill="none" stroke="var(--mist)" stroke-width="9">
      <circle cx="328" cy="249" r="24"/>
      <circle cx="352" cy="265" r="24"/>
    </g>
    <g fill="none" stroke="var(--mist)" stroke-width="10">
      <circle cx="62" cy="370" r="34"/>
      <line x1="62" y1="404" x2="62" y2="460"/>
      <line x1="40" y1="437" x2="88" y2="437"/>
    </g>
  </svg>

  <h1 class="headline" style="top:44px;">
    <span class="headline__main" style="font-size:35px;">Psychotherapy</span>
    <span class="headline__sub" style="font-size:22.5px; margin-top:7px;">for Individuals, Couples</span>
    <span class="headline__sub" style="font-size:22.5px; margin-top:8px;">and Families</span>
  </h1>

  <ul class="services" style="top:0; font-size:22px;">
    <li style="top:198px;">Parenting</li>
    <li style="top:232px;">Depression</li>
    <li style="top:265px;">Anxiety</li>
    <li style="top:299px;">Life Transitions</li>
    <li style="top:332px;">Divorce</li>
    <li style="top:366px;">Couples Issues</li>
    <li style="top:399px;">Women’s Issues</li>
    <li style="top:433px;">Attachment and</li>
    <li style="top:462px;">Neuroscience</li>
  </ul>

  <div class="portrait" style="left:21px; top:517px; width:105px; height:106px;" role="img" aria-label="Portrait photo of the therapist"></div>

  <div class="therapist-name" style="left:141px; top:562px; font-size:23px;">DANA REED, MA, MFT</div>

  <div class="contact" style="left:21px; top:0;">
    <span class="contact__line" style="top:654px; font-size:15px;">418 Harbor Lane, Cedar Grove, CA 94000</span>
    <span class="contact__line contact__web" style="top:675px; font-size:15px;">www.danareed.com</span>
    <span class="contact__line" style="top:697px; font-size:15px;">dana@danareed.com</span>
    <span class="contact__line contact__phone" style="top:718px; font-size:16px;">415.555.0182</span>
  </div>

  <div class="license" style="right:13px; top:746px;">License# MFC48210</div>
</section>

</body>
</html>
```